Brindle Offers is an online marketing platform.

A daily deals site for consumers a way to bring in new clients for clients and this is who the business cards are for. Industries - Food and Drink, Things To Do, Beauty and Spas, Staycations and Services.
Logo on one side.
Name - Owen Radley
Job Title - Sales Director
Phone Number - 07912358046
Email - owen@brindleoffers.co.uk
need same for second person
Name - Fiona Bracken
Job Title - Operations Director
Phone Number - 01632840275
Email - fiona@brindleoffers.co.uk
Bottom Right - Chatterbook Icon, Snapa Icon, Pipline Icon
Target Market(s)
Business owners of the above industries
Contact Information for Business Card
Name - Owen Radley
Name - Fiona Bracken
Look and feel

```html
<!DOCTYPE html>
<html lang="en">
<head>
<meta charset="utf-8">
<title>Brindle Offers business cards</title>
<link rel="stylesheet" href="https://fonts.googleapis.com/css2?family=Exo+2:wght@400;600&display=swap">
<style>
  :root {
    --backdrop: #00ffff;
    --card: #ffffff;
    --brand-blue: #0656a6;
    --ink: #1c1c1c;
    --ghost: #e8eff8;
  }
  * { box-sizing: border-box; margin: 0; padding: 0; }
  html, body { width: 1016px; height: 1200px; overflow: hidden; }
  body { background: var(--backdrop); position: relative; font-family: "Exo 2", sans-serif; color: var(--ink); }

  .card {
    position: absolute; left: 0; width: 1016px; height: 581px;
    background: var(--card); border-radius: 44px; overflow: hidden;
  }
  .card--owen { top: 0; }
  .card--fiona { top: 619px; }

  .ghost-ring { position: absolute; left: 80px; top: 309px; width: 262px; height: 262px; }

  .brand {
    position: absolute; left: 0; top: 120px; width: 1016px;
    display: flex; align-items: center; justify-content: center; gap: 22px;
  }
  .brand-dot { width: 116px; height: 116px; border-radius: 50%; background: var(--brand-blue); flex: none; }
  .brand-name { font-weight: 600; font-size: 64px; line-height: 1; color: var(--brand-blue); white-space: nowrap; }

  .person { position: absolute; left: 0; top: 382px; text-align: right; }
  .card--owen .person { width: 416px; }
  .card--fiona .person { width: 434px; }
  .person-name { font-weight: 600; font-size: 43px; line-height: 1; color: var(--brand-blue); white-space: nowrap; }
  .person-role { font-weight: 400; font-size: 24px; line-height: 1; color: var(--ink); white-space: nowrap; }

  .divider { position: absolute; left: 505px; top: 372px; width: 3px; height: 71px; background: var(--ink); }

  .contacts { position: absolute; left: 577px; top: 374px; list-style: none; }
  .contact { display: flex; align-items: center; gap: 8px; font-size: 28px; line-height: 41px; color: var(--ink); white-space: nowrap; }
  .contact svg { width: 28px; height: 28px; flex: none; }

  .footer-band { position: absolute; left: 0; top: 500px; width: 1016px; height: 81px; }

  .socials { position: absolute; top: 535px; left: 847px; display: flex; gap: 6px; }
  .social { width: 28px; height: 28px; border-radius: 50%; background: var(--brand-blue); }
</style>
</head>
<body>

<section class="card card--owen">
  <svg class="ghost-ring" viewBox="0 0 262 262" aria-hidden="true"><circle cx="131" cy="131" r="124" fill="none" stroke="var(--ghost)" stroke-width="10"/></svg>
  <div class="brand">
    <span class="brand-dot"></span>
    <span class="brand-name">Brindle Offers</span>
  </div>
  <div class="person">
    <p class="person-name">Owen Radley</p>
    <p class="person-role">Sales Director</p>
  </div>
  <span class="divider"></span>
  <ul class="contacts">
    <li class="contact">
      <svg viewBox="0 0 28 28" aria-hidden="true"><circle cx="14" cy="14" r="14" fill="var(--brand-blue)"/><path d="M9 7.5c1-.6 1.8-.4 2.3.5l1.2 2.3c.4.8.2 1.4-.5 1.9l-.8.6c.7 1.7 2 3 3.7 3.8l.6-.8c.5-.7 1.2-.9 1.9-.5l2.3 1.2c.9.5 1.1 1.3.5 2.3-.9 1.6-2.4 2.1-4.2 1.4-3.6-1.4-6.1-4-7.5-7.5-.6-1.7-.2-3.3 1.5-4.2z" fill="#fff"/></svg>
      <span>07912358046</span>
    </li>
    <li class="contact">
      <svg viewBox="0 0 28 28" aria-hidden="true"><circle cx="14" cy="14" r="14" fill="var(--brand-blue)"/><rect x="7.5" y="9" width="13" height="10" rx="1.5" fill="#fff"/><path d="M8.5 10.5l5.5 4.3 5.5-4.3" fill="none" stroke="var(--brand-blue)" stroke-width="1.6"/></svg>
      <span>owen@brindleoffers.co.uk</span>
    </li>
  </ul>
  <svg class="footer-band" viewBox="0 0 1016 81" aria-hidden="true">
    <path d="M0 19 L566 18 C570 20 566 30 556 35 L0 32 Z" fill="var(--brand-blue)"/>
    <path d="M0 53 L540 54 C566 53 576 20 606 18 L1016 16 L1016 81 L0 81 Z" fill="var(--ink)"/>
  </svg>
  <div class="socials">
    <span class="social" role="img" aria-label="Pipline"></span>
    <span class="social" role="img" aria-label="Chatterbook"></span>
    <span class="social" role="img" aria-label="Snapa"></span>
  </div>
</section>

<section class="card card--fiona">
  <svg class="ghost-ring" viewBox="0 0 262 262" aria-hidden="true"><circle cx="131" cy="131" r="124" fill="none" stroke="var(--ghost)" stroke-width="10"/></svg>
  <div class="brand">
    <span class="brand-dot"></span>
    <span class="brand-name">Brindle Offers</span>
  </div>
  <div class="person">
    <p class="person-name">Fiona Bracken</p>
    <p class="person-role">Operations Director</p>
  </div>
  <span class="divider"></span>
  <ul class="contacts">
    <li class="contact">
      <svg viewBox="0 0 28 28" aria-hidden="true"><circle cx="14" cy="14" r="14" fill="var(--brand-blue)"/><path d="M9 7.5c1-.6 1.8-.4 2.3.5l1.2 2.3c.4.8.2 1.4-.5 1.9l-.8.6c.7 1.7 2 3 3.7 3.8l.6-.8c.5-.7 1.2-.9 1.9-.5l2.3 1.2c.9.5 1.1 1.3.5 2.3-.9 1.6-2.4 2.1-4.2 1.4-3.6-1.4-6.1-4-7.5-7.5-.6-1.7-.2-3.3 1.5-4.2z" fill="#fff"/></svg>
      <span>01632840275</span>
    </li>
    <li class="contact">
      <svg viewBox="0 0 28 28" aria-hidden="true"><circle cx="14" cy="14" r="14" fill="var(--brand-blue)"/><rect x="7.5" y="9" width="13" height="10" rx="1.5" fill="#fff"/><path d="M8.5 10.5l5.5 4.3 5.5-4.3" fill="none" stroke="var(--brand-blue)" stroke-width="1.6"/></svg>
      <span>fiona@brindleoffers.co.uk</span>
    </li>
  </ul>
  <svg class="footer-band" viewBox="0 0 1016 81" aria-hidden="true">
    <path d="M0 19 L566 18 C570 20 566 30 556 35 L0 32 Z" fill="var(--brand-blue)"/>
    <path d="M0 53 L540 54 C566 53 576 20 606 18 L1016 16 L1016 81 L0 81 Z" fill="var(--ink)"/>
  </svg>
  <div class="socials">
    <span class="social" role="img" aria-label="Pipline"></span>
    <span class="social" role="img" aria-label="Chatterbook"></span>
    <span class="social" role="img" aria-label="Snapa"></span>
  </div>
</section>

</body>
</html>
```